Business Card Design Project

Velvet Harbor is a Boutique Clothing. On the business cards I would like to have this included
Website: www.velvetharbor-example.com
Email: shop@velvetharbor-example.com
Owner: Mira Sol & Tor Dell

Industry/Entity Type

Business

Contact Information for Business Card

I wanted something simple and elegant. I have attach business logo.

```html
<!DOCTYPE html>
<html lang="en">
<head>
<meta charset="utf-8">
<title>Velvet Harbor — Business Card</title>
<link href="https://fonts.googleapis.com/css2?family=Questrial&family=Tinos:ital,wght@1,400&display=swap" rel="stylesheet">
<style>
  :root {
    --page-bg: #d9d4cd;
    --card-top: #f4f4f4;
    --card-bottom: #e6e4e2;
    --ink: #1b1b1b;
    --band: #0d0d0d;
    --silver: #b9b6b2;
    --rule: #2a2a2a;
  }
  * { margin: 0; padding: 0; box-sizing: border-box; }
  html, body {
    width: 1200px; height: 970px; overflow: hidden;
    background: var(--page-bg);
  }
  .card {
    position: absolute; left: 80px; top: 190px;
    width: 1040px; height: 590px;
    border-radius: 24px; overflow: hidden;
    background: linear-gradient(180deg, var(--card-top), var(--card-bottom));
    box-shadow: 0 12px 30px rgba(0,0,0,0.18);
  }
  .card-wave { position: absolute; inset: 0; width: 1040px; height: 590px; }
  .brand {
    position: absolute; left: 238px; top: 300px;
    transform: translate(-50%, -50%);
    display: flex; align-items: center; gap: 14px;
    font-family: "Questrial", sans-serif; font-size: 34px;
    letter-spacing: 3px; color: var(--ink); white-space: nowrap;
  }
  .brand-dot { width: 14px; height: 14px; border-radius: 50%; background: var(--ink); }
  .divider {
    position: absolute; left: 443px; top: 135px;
    width: 2px; height: 262px; background: var(--rule);
  }
  .owners {
    position: absolute; left: 518px; top: 130px;
    font-family: "Tinos", serif; font-style: italic;
    font-size: 38px; color: var(--ink); white-space: nowrap;
  }
  .role {
    position: absolute; left: 520px; top: 172px;
    font-family: "Questrial", sans-serif; font-size: 22px; color: var(--ink);
  }
  .contact {
    position: absolute; left: 516px;
    display: flex; align-items: center; gap: 10px;
    font-family: "Questrial", sans-serif; font-size: 24px; color: var(--ink);
  }
  .contact-email { top: 328px; }
  .contact-web { top: 368px; }
  .contact svg { width: 30px; height: 30px; flex: none; }
</style>
</head>
<body>
  <div class="card">
    <svg class="card-wave" viewBox="0 0 1040 590" aria-hidden="true">
      <path d="M0 455 C 220 500, 380 540, 560 520 C 760 500, 900 445, 1025 445 L 1025 452 C 900 452, 760 510, 560 532 C 380 550, 220 512, 0 470 Z" fill="var(--silver)"/>
      <path d="M0 472 C 200 520, 340 545, 520 535 C 720 522, 880 455, 1040 450 L 1040 590 L 0 590 Z" fill="var(--band)"/>
    </svg>

    <div class="brand"><span class="brand-dot"></span>VELVET HARBOR</div>

    <div class="divider"></div>

    <div class="owners">Mira Sol &amp; Tor Dell</div>
    <div class="role">Owner</div>

    <div class="contact contact-email">
      <svg viewBox="0 0 30 30" aria-hidden="true">
        <circle cx="15" cy="15" r="13" fill="none" stroke="var(--ink)" stroke-width="2"/>
        <rect x="8" y="10" width="14" height="10" rx="1" fill="var(--ink)"/>
        <path d="M8 10 L15 16 L22 10" fill="none" stroke="#f0f0f0" stroke-width="1.4"/>
      </svg>
      shop@velvetharbor-example.com
    </div>
    <div class="contact contact-web">
      <svg viewBox="0 0 30 30" aria-hidden="true">
        <circle cx="15" cy="15" r="13" fill="none" stroke="var(--ink)" stroke-width="2"/>
        <circle cx="15" cy="15" r="8" fill="none" stroke="var(--ink)" stroke-width="1.5"/>
        <ellipse cx="15" cy="15" rx="3.5" ry="8" fill="none" stroke="var(--ink)" stroke-width="1.3"/>
        <path d="M7 15 H23 M8.5 11 H21.5 M8.5 19 H21.5" stroke="var(--ink)" stroke-width="1.2"/>
      </svg>
      www.velvetharbor-example.com
    </div>
  </div>
</body>
</html>
```